Wickedmarlo.com adult webpage with links to various sites she is on.

UPDATE 3/10- let’s keep this a bit more simple. I am uploading three pics and a sketch of how she wants her site to look. It’s really just a page that has her links.

Looking to set up a homepage for my hot wife that has her clickable links on there. Pehaps a space for an about me and some notes encouraging audience to click and join peek vault.
Cashwix link:

https://peekvault.com/away?url=https://Cashwix.com/wickedmarlo

Here is some
Copy from her:
“Queen of Dirty Talk” is important to work in.
🔥HOTWIFE SUPER SLUT🔥

...... I do things the other girls don’t! I suck and fuck like no other woman you’ll ever see. Filthy dirty talk, lots of sloppy oral, fantasy role play, dress up and cum swallowing.

Cum watch me! Have your mind..... and your big fat load blown away!

💋This page is where you will find ALL my links. My free peekvault has my videos for sale. My VIP page you will get the same videos at a discounted prices, plus lots of juicy extras. I also answer all my messages there. Make sure to check out my VIP page today so you don’t miss out on any of the fun!💋💋💋
Updates

I am tryin go to extend the project time to at least two weeks. I just don’t know how to edit. I have an email out to support.

Target Market(s)

Adult entertainment

Industry/Entity Type

Porn

Coding

Coded - Design and coding required

Number of Pages Required

1 page

Colors
000000
eea4c8

Requirements
Must have
• WickedMarlo (no space between) is her stage name.
She would like maybe some cute horns in the logo. Maybe make the “S” have little devil horns on top and roll the bottom of the “S” like a devil tail with the arrows/spade point at at end.
A hot pic of her in background.
Buttons to her various pages.
Nice to have
• Perhaps an about me drop down or window we can write copy for? Pink black and leopard are good color choices.

```html
<!DOCTYPE html>
<html lang="en">
<head>
<meta charset="utf-8">
<title>WickedMarlo</title>
<link href="https://fonts.googleapis.com/css2?family=Montserrat:wght@400;600;700;800&family=Open+Sans:wght@400;600&display=swap" rel="stylesheet">
<style>
:root{
  --pink:#eea4c8;
  --pink-deep:#d9789f;
  --black:#000;
  --dark:#141414;
  --panel:#1c1c1c;
  --white:#fff;
  --ink:#222;
  --muted:#555;
  --line:#d6d6d6;
}
*{box-sizing:border-box;margin:0;padding:0}
html,body{width:1200px;height:2536px;overflow:hidden}
body{position:relative;background:var(--white);font-family:"Open Sans",Arial,sans-serif;color:var(--ink)}

.hero{position:absolute;left:0;top:0;width:1200px;height:470px;overflow:hidden}
.hero-photo{position:absolute;inset:0;background:linear-gradient(100deg,#3a3a3a 0%,#1a1a1a 35%,#4a4a4a 60%,#262626 100%)}
.hero-curve{position:absolute;left:0;bottom:0}
.site-header{position:absolute;left:0;top:0;width:1200px;height:62px;background:rgba(0,0,0,.55);display:flex;align-items:center;padding:0 40px}
.logo{font-family:"Montserrat",sans-serif;font-weight:700;font-size:34px;color:var(--pink);letter-spacing:.5px}
.main-nav{margin-left:auto;display:flex;gap:40px;align-items:center;font-family:"Montserrat",sans-serif;font-size:12px;font-weight:600;color:var(--white);letter-spacing:1px}
.main-nav .active{border-bottom:2px solid var(--pink);padding-bottom:4px}
.vip-btn{background:var(--pink);color:var(--black);padding:8px 16px;border-radius:2px}
.hero-title{position:absolute;left:760px;top:248px;width:330px;font-family:"Montserrat",sans-serif;font-weight:800;font-size:38px;line-height:42px;color:var(--white);text-align:right}
.hero-btn{position:absolute;left:852px;top:346px;height:38px;padding:0 18px;background:var(--black);color:var(--white);font-family:"Montserrat",sans-serif;font-weight:600;font-size:13px;display:flex;align-items:center;gap:10px;letter-spacing:.5px}
.hero-arrow{position:absolute;top:322px}

.intro{position:absolute;left:0;top:470px;width:1200px;text-align:center}
.intro-lead{margin-top:86px;font-family:"Montserrat",sans-serif;font-weight:600;font-size:30px;color:var(--pink-deep)}
.intro-title{margin-top:18px;font-family:"Montserrat",sans-serif;font-weight:700;font-size:24px;color:var(--black)}
.intro p{width:860px;margin:14px auto 0;font-size:13px;line-height:22px;color:var(--muted)}

.gallery{position:absolute;left:0;top:905px;width:1200px;height:825px;background:var(--dark)}
.tabs{text-align:center;margin-top:22px;font-family:"Montserrat",sans-serif;font-weight:600;font-size:26px;color:var(--white)}
.tabs .current{color:var(--pink);border-bottom:3px solid var(--pink)}
.grid{position:absolute;left:12px;top:94px;width:1176px;display:grid;grid-template-columns:repeat(4,1fr);gap:10px}
.thumb{position:relative;height:240px;background:linear-gradient(135deg,#6a6a6a,#2c2c2c)}
.thumb.warm{background:linear-gradient(135deg,#c9643a,#3d1a10)}
.thumb-tag{position:absolute;left:8px;top:6px;font-size:11px;font-weight:600;color:var(--white)}
.thumb-play{position:absolute;right:6px;bottom:6px}
.view-all{position:absolute;left:536px;top:726px;width:128px;height:46px;border:1px solid var(--white);color:var(--white);font-family:"Montserrat",sans-serif;font-weight:600;font-size:13px;display:flex;align-items:center;justify-content:center;letter-spacing:1px}

.contact{position:absolute;left:0;top:1730px;width:1200px;height:440px;text-align:center}
.contact h2{margin-top:66px;font-family:"Montserrat",sans-serif;font-weight:600;font-size:32px;color:var(--pink-deep)}
.form{width:612px;margin:28px auto 0;display:grid;grid-template-columns:1fr 1fr;gap:16px 18px}
.field{height:40px;border:1px solid var(--line);font-size:12px;color:#999;text-align:left;padding:11px 12px}
.field.wide{grid-column:1/3;height:84px}
.submit{grid-column:1/3;justify-self:center;width:124px;height:44px;background:var(--pink);color:var(--white);font-family:"Montserrat",sans-serif;font-weight:700;font-size:13px;display:flex;align-items:center;justify-content:center;margin-top:6px}

.follow{position:absolute;left:0;top:2170px;width:1200px;height:278px;background:var(--pink);text-align:center}
.follow h2{margin-top:60px;font-family:"Montserrat",sans-serif;font-weight:600;font-size:36px;color:var(--white)}
.socials{margin-top:40px;display:flex;justify-content:center;gap:46px}
.social{width:72px;height:72px;border-radius:50%;background:var(--white);display:flex;align-items:center;justify-content:center;font-family:"Montserrat",sans-serif;font-weight:600;font-size:11px;color:var(--pink-deep)}

.site-footer{position:absolute;left:0;top:2448px;width:1200px;height:88px;background:var(--black);display:flex;align-items:center;padding:0 40px;justify-content:space-between}
.site-footer small{font-size:12px;color:#999}
</style>
</head>
<body>

<section class="hero">
  <div class="hero-photo" role="img" aria-label="Moody black and white photo of the model lying in bed"></div>
  <header class="site-header">
    <div class="logo">WickedMarlo</div>
    <nav class="main-nav">
      <span class="active">HOME</span><span>PHOTOS</span><span>SOCIAL MEDIA</span><span>ABOUT ME</span><span>CONTACT</span>
      <span class="vip-btn">♥ VIP PAGE</span>
    </nav>
  </header>
  <svg class="hero-arrow" style="left:40px" width="30" height="40" viewBox="0 0 30 40"><path d="M20 8 L8 20 L20 32" fill="none" stroke="#fff" stroke-width="4"/></svg>
  <svg class="hero-arrow" style="left:1130px" width="30" height="40" viewBox="0 0 30 40"><path d="M10 8 L22 20 L10 32" fill="none" stroke="#fff" stroke-width="4"/></svg>
  <h1 class="hero-title">HOT WIFE<br>SUPER SLUT</h1>
  <div class="hero-btn"><svg width="16" height="16" viewBox="0 0 16 16"><circle cx="8" cy="8" r="8" fill="#fff"/><path d="M6 4.5 L11 8 L6 11.5Z" fill="#000"/></svg>VIEW MY VIDEOS</div>
  <svg class="hero-curve" width="1200" height="110" viewBox="0 0 1200 110"><path d="M0 10 Q600 150 1200 10 L1200 110 L0 110Z" fill="#fff"/></svg>
</section>

<section class="intro">
  <h2 class="intro-lead">“Queen of Dirty Talk” is important to work in.</h2>
  <h3 class="intro-title">HOT WIFE SUPER SLUT</h3>
  <p>...... I do things the other girls don’t! I suck and fuck like no other woman you’ll ever see. Filthy dirty talk, lots of sloppy oral, fantasy role play, dress up and cum swallowing.</p>
  <p>Cum watch me! Have your mind..... and your big fat load blown away!</p>
  <p>This page is where you will find ALL my links. My free peekvault has my videos for sale. My VIP page you will get the same videos at a discounted prices, plus lots of juicy extras. I also answer all my messages there. Make sure to check out my VIP page today so you don’t miss out on any of the fun!</p>
</section>

<section class="gallery">
  <div class="tabs">All &nbsp;|&nbsp; Photos &nbsp;|&nbsp; <span class="current">Videos</span></div>
  <div class="grid">
    <div class="thumb" role="img" aria-label="Video preview"><span class="thumb-tag">VID</span><svg class="thumb-play" width="20" height="20" viewBox="0 0 20 20"><path d="M5 3 L17 10 L5 17Z" fill="#fff"/></svg></div>
    <div class="thumb" role="img" aria-label="Video preview"><span class="thumb-tag">VID</span><svg class="thumb-play" width="20" height="20" viewBox="0 0 20 20"><path d="M5 3 L17 10 L5 17Z" fill="#fff"/></svg></div>
    <div class="thumb warm" role="img" aria-label="Video preview in warm colour"><span class="thumb-tag">VID</span><svg class="thumb-play" width="20" height="20" viewBox="0 0 20 20"><path d="M5 3 L17 10 L5 17Z" fill="#fff"/></svg></div>
    <div class="thumb" role="img" aria-label="Video preview"><span class="thumb-tag">VID</span><svg class="thumb-play" width="20" height="20" viewBox="0 0 20 20"><path d="M5 3 L17 10 L5 17Z" fill="#fff"/></svg></div>
    <div class="thumb" role="img" aria-label="Video preview"><span class="thumb-tag">VID</span><svg class="thumb-play" width="20" height="20" viewBox="0 0 20 20"><path d="M5 3 L17 10 L5 17Z" fill="#fff"/></svg></div>
    <div class="thumb" role="img" aria-label="Video preview"><span class="thumb-tag">VID</span><svg class="thumb-play" width="20" height="20" viewBox="0 0 20 20"><path d="M5 3 L17 10 L5 17Z" fill="#fff"/></svg></div>
    <div class="thumb" role="img" aria-label="Video preview"><span class="thumb-tag">VID</span><svg class="thumb-play" width="20" height="20" viewBox="0 0 20 20"><path d="M5 3 L17 10 L5 17Z" fill="#fff"/></svg></div>
    <div class="thumb" role="img" aria-label="Video preview"><span class="thumb-tag">VID</span><svg class="thumb-play" width="20" height="20" viewBox="0 0 20 20"><path d="M5 3 L17 10 L5 17Z" fill="#fff"/></svg></div>
  </div>
  <div class="view-all">VIEW ALL</div>
</section>

<section class="contact">
  <h2>Message Me</h2>
  <div class="form">
    <div class="field">Full Name</div>
    <div class="field">Email Address</div>
    <div class="field wide">Message</div>
    <div class="submit">SUBMIT</div>
  </div>
</section>

<section class="follow">
  <h2>Follow me</h2>
  <div class="socials">
    <div class="social">Fanlink</div>
    <div class="social">Streamly</div>
    <div class="social">Cashwix</div>
    <div class="social">Picshare</div>
  </div>
</section>

<footer class="site-footer">
  <small>Copyright © 2021 WickedMarlo. All rights reserved.</small>
  <svg width="32" height="32" viewBox="0 0 32 32"><circle cx="16" cy="16" r="15" fill="#333"/><path d="M10 19 L16 12 L22 19" fill="none" stroke="#fff" stroke-width="2.5"/></svg>
</footer>

</body>
</html>
```